Stationery Design Project for Explainer Video Company

We are a company for explainer videos. We are working together with a community consisting of creative people. The plumtiko videos are animated. Please visit our homepage at www.plumtiko.example, we like our Monitor-Logo, so please create a similar stationary to that. you might use the colours and the font (Pacifico or similar)
We need business cards too. We don't need Facsimile
attached is the logo (please don't use chatterbox text)

Target Market(s)

Marketing, SMB

Industry/Entity Type

Business

```html
<!DOCTYPE html>
<html lang="en">
<head>
<meta charset="utf-8">
<title>plumtiko stationery</title>
<link rel="stylesheet" href="https://fonts.googleapis.com/css2?family=Pacifico&family=Archivo+Black&family=Open+Sans:wght@700&display=swap">
<style>
  :root {
    --backdrop: #cbc2a6;
    --paper: #ffffff;
    --brand-red: #d00000;
    --brand-blue: #3dbde9;
    --ink: #000000;
    --silver: #c9d0cf;
    --info-tint: #f4f6fb;
  }
  * { margin: 0; padding: 0; box-sizing: border-box; }
  html, body { width: 1200px; height: 960px; overflow: hidden; }
  body { background: var(--backdrop); position: relative; font-family: "Open Sans", sans-serif; }

  .sheet, .card { position: absolute; background: var(--paper); overflow: hidden; }
  .sheet svg, .card svg { position: absolute; left: 0; display: block; }

  .letterhead { left: 94px; top: 40px; width: 593px; height: 835px; }
  .letterhead .head-band { top: 0; width: 593px; height: 130px; }
  .letterhead .foot-band { bottom: 0; width: 593px; height: 85px; }

  .brand { position: absolute; display: flex; align-items: center; white-space: nowrap; }
  .brand-mark { background: var(--brand-red); border-radius: 8px; flex: none; }
  .brand-name { font-family: "Pacifico", cursive; color: var(--brand-blue); line-height: 1; font-weight: 400; }

  .letterhead .brand { left: 52px; top: 18px; gap: 14px; }
  .letterhead .brand-mark { width: 60px; height: 60px; background: var(--paper); border: 5px solid var(--ink); }
  .letterhead .brand-name { font-size: 40px; }
  .letterhead .foot-mark { position: absolute; right: 48px; bottom: 22px; width: 40px; height: 40px; background: var(--brand-red); border-radius: 7px; }

  .card-back { left: 730px; top: 125px; width: 315px; height: 173px; }
  .card-back .brand { left: 34px; top: 24px; gap: 12px; }
  .card-back .brand-mark { width: 68px; height: 68px; }
  .card-back .brand-name { font-size: 44px; }
  .card-back .card-band { bottom: 0; width: 315px; height: 50px; }

  .card-front { left: 705px; top: 320px; width: 315px; height: 175px; }
  .card-front .info-panel { position: absolute; left: 160px; top: 18px; width: 145px; height: 75px; background: var(--info-tint); }
  .card-front .brand { left: 12px; top: 84px; gap: 6px; }
  .card-front .brand-mark { width: 32px; height: 32px; border-radius: 5px; }
  .card-front .brand-name { font-size: 21px; }
  .card-front .info-text { position: absolute; left: 160px; top: 78px; font-size: 11px; font-weight: 700; color: var(--ink); white-space: nowrap; }
  .card-front .card-band { bottom: 0; width: 315px; height: 80px; }

  .side-label { position: absolute; left: 1034px; top: 458px; font-family: "Archivo Black", sans-serif; font-size: 18px; color: var(--ink); }
</style>
</head>
<body>

<section class="sheet letterhead" aria-label="Letterhead">
  <svg class="head-band" viewBox="0 0 593 130" aria-hidden="true">
    <defs>
      <linearGradient id="head-silver" x1="0" y1="0" x2="1" y2="0">
        <stop offset="0" stop-color="#c3cccb"/>
        <stop offset="0.35" stop-color="#ffffff"/>
      </linearGradient>
    </defs>
    <path d="M0 60 L0 128 C150 88 330 72 593 76 L593 0 Z" fill="url(#head-silver)"/>
    <path d="M430 62 C500 56 560 42 593 30 V92 C550 76 490 64 430 62 Z" fill="var(--ink)"/>
    <path d="M0 0 H593 V30 C450 62 260 96 0 72 Z" fill="var(--brand-red)"/>
  </svg>
  <div class="brand">
    <span class="brand-mark"></span>
    <span class="brand-name">plumtiko</span>
  </div>
  <svg class="foot-band" viewBox="0 0 593 85" aria-hidden="true">
    <defs>
      <linearGradient id="foot-silver" x1="0" y1="0" x2="1" y2="0">
        <stop offset="0" stop-color="#c9d0cf"/>
        <stop offset="0.55" stop-color="#ffffff"/>
        <stop offset="1" stop-color="#0a0a0a"/>
      </linearGradient>
    </defs>
    <path d="M0 70 C200 36 420 16 593 12 V85 H0 Z" fill="url(#foot-silver)"/>
    <path d="M0 45 C200 12 420 0 593 0 V12 C420 16 200 36 0 70 Z" fill="var(--brand-red)"/>
  </svg>
  <span class="foot-mark"></span>
</section>

<section class="card card-back" aria-label="Business card back">
  <div class="brand">
    <span class="brand-mark"></span>
    <span class="brand-name">plumtiko</span>
  </div>
  <svg class="card-band" viewBox="0 0 315 50" aria-hidden="true">
    <defs>
      <linearGradient id="back-silver" x1="0" y1="0" x2="1" y2="0">
        <stop offset="0" stop-color="#c9d0cf"/>
        <stop offset="0.55" stop-color="#ffffff"/>
        <stop offset="1" stop-color="#111111"/>
      </linearGradient>
    </defs>
    <path d="M0 40 C100 18 220 8 315 6 V50 H0 Z" fill="url(#back-silver)"/>
    <path d="M0 28 C100 10 220 2 315 2 V8 C220 10 100 20 0 40 Z" fill="var(--brand-red)"/>
  </svg>
</section>

<section class="card card-front" aria-label="Business card front">
  <div class="info-panel"></div>
  <div class="brand">
    <span class="brand-mark"></span>
    <span class="brand-name">plumtiko</span>
  </div>
  <p class="info-text">space for information</p>
  <svg class="card-band" viewBox="0 0 315 80" aria-hidden="true">
    <defs>
      <linearGradient id="front-red" x1="0" y1="0" x2="1" y2="0">
        <stop offset="0" stop-color="#ffffff"/>
        <stop offset="0.55" stop-color="var(--brand-red)"/>
        <stop offset="1" stop-color="var(--brand-red)"/>
      </linearGradient>
    </defs>
    <path d="M200 30 C250 16 290 8 315 4 V28 C280 30 240 32 200 30 Z" fill="#d6dbda"/>
    <path d="M0 50 C70 60 130 60 170 56 L0 80 Z" fill="var(--ink)"/>
    <path d="M0 80 C110 58 220 36 315 22 V80 Z" fill="url(#front-red)"/>
  </svg>
</section>

<p class="side-label">front</p>

</body>
</html>
```